Rising Side by Side A Handbook to Guide Managers and Crews Toward Greater Levels of Output

We need a book cover design for a book titled: Rising Side by Side:
A Handbook to Guide Managers and Crews Toward Greater Levels of Output
The book is intended to enhance the author's personal brand and promote the author's consulting services. The book also teaches: How To Help Leaders and Teams Reach New Heights of Performance. I would like to use the colors from the www.brindlemoorworks.example website (blue and orange). The design should communicate credibility and expertise in the topic of the book.

Target Market(s)

Municipal and Industrial and Energy Industry Team Leaders and Teams

Industry/Entity Type

water and waste water, energy, power generation, petrochmical

Requirements
Must have
• Look like a Dalbrook Ledger best seller. Look professional and appealling
Nice to have
• Sell at the airport. Executives keep in their office.
Should not have
• Do not plagiarize.

```html
<!DOCTYPE html>
<html lang="en">
<head>
<meta charset="utf-8">
<title>Rising Side by Side — Book Cover</title>
<link rel="stylesheet" href="https://fonts.googleapis.com/css2?family=Oswald:wght@400;500;700&family=Tinos:wght@400;700&display=swap">
<style>
  :root {
    --navy: #0b2a63;
    --blue: #2f86d6;
    --orange: #f08c1e;
    --paper: #f2f3f5;
    --ink: #1b2233;
    --white: #ffffff;
  }
  * { box-sizing: border-box; margin: 0; padding: 0; }
  html, body { width: 1200px; height: 926px; overflow: hidden; background: var(--white); }
  .canvas { position: relative; width: 1200px; height: 926px; background: var(--white); }

  .book-spread { position: absolute; left: 50px; top: 53px; width: 1100px; height: 820px; display: flex; box-shadow: 0 10px 30px rgba(0,0,0,.15); }

  /* shared pieces */
  .band-navy { position: absolute; left: 0; right: 0; background: var(--navy); }
  .stripe { position: absolute; left: 0; right: 0; height: 7px; }
  .stripe--blue { background: var(--blue); }
  .stripe--orange { background: var(--orange); }
  .brand { display: flex; align-items: center; gap: 6px; font-family: "Oswald", sans-serif; font-weight: 500; color: var(--white); letter-spacing: 2px; text-transform: uppercase; white-space: nowrap; }
  .brand__dot { width: 10px; height: 10px; border-radius: 50%; background: var(--white); }

  /* back cover */
  .back-cover { position: relative; width: 520px; height: 820px; background: var(--paper); overflow: hidden; }
  .back-cover .band-navy--top { top: 0; height: 120px; display: flex; align-items: center; justify-content: center; }
  .back-cover .band-navy--top .brand { font-size: 16px; }
  .back-cover .stripe--top { top: 120px; }
  .back-title { position: absolute; top: 150px; left: 30px; right: 30px; text-align: center; font-family: "Oswald", sans-serif; color: var(--navy); line-height: 1.2; }
  .back-title__main { font-weight: 700; font-size: 26px; }
  .back-title__sub { font-weight: 400; font-size: 21px; }
  .back-title__author { font-weight: 400; font-size: 21px; color: var(--orange); }
  .back-portrait { position: absolute; top: 300px; left: 190px; width: 140px; height: 140px; border-radius: 50%; border: 2px solid var(--navy); background: radial-gradient(circle at 50% 35%, #8a5a3c 0 22%, #3a3030 48%, #e9eaec 49%); }
  .back-blurb { position: absolute; top: 462px; left: 40px; right: 40px; font-family: "Oswald", sans-serif; font-size: 11px; line-height: 1.35; color: var(--ink); }
  .back-blurb p { margin-bottom: 10px; }
  .back-blurb strong { color: var(--navy); font-weight: 700; }
  .back-cover .stripe--orange { top: 713px; }
  .back-cover .band-navy--bottom { top: 720px; height: 100px; }
  .back-cover .stripe--bottom { bottom: 0; }

  /* spine */
  .spine { position: relative; width: 60px; height: 820px; background: var(--paper); border-left: 1px solid #d8dbe0; border-right: 1px solid #d8dbe0; overflow: hidden; }
  .spine .band-navy--top { top: 0; height: 120px; display: flex; align-items: center; justify-content: center; }
  .spine .brand { writing-mode: vertical-rl; transform: rotate(180deg); font-size: 11px; }
  .spine .stripe--top { top: 120px; }
  .spine__title { position: absolute; top: 140px; bottom: 20px; left: 0; right: 0; display: flex; flex-direction: column; justify-content: center; align-items: flex-start; writing-mode: vertical-rl; transform: rotate(180deg); font-family: "Oswald", sans-serif; font-weight: 700; text-transform: uppercase; color: var(--navy); letter-spacing: 1.5px; white-space: nowrap; line-height: 1.2; }
  .spine__line--main { display: block; font-size: 17px; }
  .spine__line--sub { display: block; font-size: 10.5px; }
  .spine__accent { color: var(--orange); }

  /* front cover */
  .front-cover { position: relative; width: 520px; height: 820px; background: var(--paper); overflow: hidden; }
  .front-cover .band-navy--top { top: 0; height: 112px; display: flex; align-items: center; justify-content: center; }
  .front-title-lead { font-family: "Oswald", sans-serif; font-weight: 700; font-size: 37px; letter-spacing: 3px; color: var(--orange); text-transform: uppercase; }
  .front-cover .stripe--top { top: 112px; }
  .author-photo { position: absolute; left: 0; top: 119px; width: 520px; height: 590px; background: linear-gradient(180deg, #e7e4e1 0%, #8c5f42 30%, #6b4a38 48%, #2f2b2c 62%, #262426 100%); clip-path: polygon(0 0, 46% 0, 46% 70%, 100% 74%, 100% 100%, 0 100%); }
  .front-title { position: absolute; top: 140px; right: 22px; text-align: left; font-family: "Oswald", sans-serif; font-weight: 700; font-size: 46px; line-height: 1.05; text-transform: uppercase; color: var(--navy); }
  .front-title__accent { color: var(--orange); }
  .front-teaser { position: absolute; left: 220px; right: 24px; top: 590px; font-family: "Tinos", serif; font-size: 17px; line-height: 1.25; color: var(--white); text-shadow: 0 1px 2px rgba(0,0,0,.5); }
  .front-brand { position: absolute; left: 24px; top: 670px; }
  .front-brand .brand { font-size: 13px; }
  .front-cover .stripe--bottom-top { top: 709px; }
  .front-cover .band-navy--bottom { top: 716px; height: 97px; display: flex; align-items: center; justify-content: center; }
  .front-author { font-family: "Tinos", serif; font-weight: 700; font-size: 40px; color: var(--white); }
  .front-cover .stripe--bottom { bottom: 0; }
</style>
</head>
<body>
<main class="canvas">
  <div class="book-spread">

    <section class="back-cover">
      <div class="band-navy band-navy--top">
        <div class="brand"><span class="brand__dot"></span>Brindlemoor Works</div>
      </div>
      <div class="stripe stripe--blue stripe--top"></div>

      <div class="back-title">
        <div class="back-title__main">Rising Side by Side:</div>
        <div class="back-title__sub">A Handbook to Guide Managers and Crews Toward Greater Levels of Output</div>
        <div class="back-title__author">Written by Darren Whitlock</div>
      </div>

      <div class="back-portrait" role="img" aria-label="Circular portrait of the author in a dark suit and red tie"></div>

      <div class="back-blurb">
        <p><strong>Darren Whitlock from Brindlemoor Works,</strong> a company specializing in driving operational excellence for municipal and industrial clients. Darren shares his childhood fascination with refineries and petrochemical plants, acknowledging their economic importance while being aware of their environmental impact.</p>
        <p><strong>He discusses his journey,</strong> from academic pursuits in science and math to gaining firsthand experience in the industry. Darren highlights the need for operational efficiency, addressing constraints such as labor shortage and technology limitations. He emphasizes Brindlemoor's role in optimizing existing systems or introducing innovative technologies to enhance efficiency, reduce environmental impact, and promote competitiveness.</p>
        <p><strong>Darren concludes by offering advice to aspiring entrepreneurs</strong> in the energy space, emphasizing the importance of understanding their "why" and exploring unique problem-solving opportunities.</p>
      </div>

      <div class="stripe stripe--orange"></div>
      <div class="band-navy band-navy--bottom"></div>
      <div class="stripe stripe--blue stripe--bottom"></div>
    </section>

    <section class="spine">
      <div class="band-navy band-navy--top">
        <div class="brand">Brindlemoor</div>
      </div>
      <div class="stripe stripe--blue stripe--top"></div>
      <div class="spine__title">
        <span class="spine__line--main">Rising Side by Side:</span>
        <span class="spine__line--sub">A Handbook to Guide Managers and Crews Toward <span class="spine__accent">Greater Levels of Output</span></span>
      </div>
    </section>

    <section class="front-cover">
      <div class="band-navy band-navy--top">
        <h1 class="front-title-lead">Rising Side by Side:</h1>
      </div>
      <div class="stripe stripe--blue stripe--top"></div>

      <div class="author-photo" role="img" aria-label="Portrait photograph of the smiling author in a dark pinstripe suit, white shirt and red tie"></div>

      <h2 class="front-title">
        A Handbook<br>to Guide<br>Managers<br>and Crews<br>Toward<br>
        <span class="front-title__accent">Greater<br>Levels of<br>Output</span>
      </h2>

      <p class="front-teaser">The book also teaches: How To Help Leaders and Teams Reach New Heights of Performance.</p>

      <div class="front-brand">
        <div class="brand"><span class="brand__dot"></span>Brindlemoor Works</div>
      </div>

      <div class="stripe stripe--blue stripe--bottom-top"></div>
      <div class="band-navy band-navy--bottom">
        <div class="front-author">Darren Whitlock</div>
      </div>
      <div class="stripe stripe--blue stripe--bottom"></div>
    </section>

  </div>
</main>
</body>
</html>
```